D*mn Those Cozy Walls - Dare Boldly, Claim Center Stage Within Every Day: UPCOMING BOOK

We want a Book Cover for a book that will be published shortly. Some options we originally created are attached but they are not really working but give an idea of the text that needs to be on there. We want it to look like a quality book. Tessa is a well known acting coach, and we have some amazing celebrity quotes for the front cover - but it doesn't HAVE to reflect the acting world, the book is for everyone. We want something that represents freedom a sense of release, INSPIRATIONAL - but not cheesy. No flowers or images like that. Simple and authentic is best... Happy to try some with text only and just block colors - the title needs to POP. It's long but we want the Dare Boldly part to pop as well.

```html
<!DOCTYPE html>
<html lang="en">
<head>
<meta charset="utf-8">
<title>D*mn Those Cozy Walls – Book Cover</title>
<link rel="stylesheet" href="https://fonts.googleapis.com/css2?family=Montserrat:wght@400;500;600;800;900&family=Allura&display=swap">
<style>
  :root {
    --stage: #d8d8d8;
    --navy: #1f2a55;
    --white: #ffffff;
    --band-dark: rgba(38, 48, 98, 0.72);
    --band-light: #f4f4f6;
    --sky-top: #2d4f86;
    --sky-mid: #4a67a8;
    --dusk: #7b6aa0;
    --mist: #8fa9dc;
    --ridge: #3d5aa0;
    --valley: #1c2a63;
  }
  * { box-sizing: border-box; margin: 0; padding: 0; }
  html, body {
    width: 1116px; height: 1200px; overflow: hidden;
    background: var(--stage);
  }
  .book-cover {
    position: absolute; left: 163px; top: 20px;
    width: 790px; height: 1160px; overflow: hidden;
    font-family: "Montserrat", sans-serif; color: var(--white);
  }
  .cover-art {
    position: absolute; inset: 0;
    background:
      radial-gradient(ellipse 60% 30% at 85% 22%, rgba(150,110,160,.75), transparent 70%),
      radial-gradient(ellipse 70% 18% at 50% 58%, rgba(190,210,240,.6), transparent 75%),
      linear-gradient(180deg, var(--sky-top) 0%, var(--sky-mid) 32%, var(--mist) 52%, var(--ridge) 70%, var(--valley) 100%);
  }
  .author-band {
    position: absolute; left: 0; right: 0; top: 62px; height: 88px;
    background: var(--band-dark);
  }
  .author-name {
    position: absolute; left: 0; right: 0; top: 66px; text-align: center;
    font-weight: 600; font-size: 50px; letter-spacing: 0.22em;
    text-shadow: 0 3px 4px rgba(0,0,0,.35);
  }
  .author-credit {
    position: absolute; left: 0; right: 0; top: 158px; text-align: center;
    font-weight: 500; font-size: 30px;
    text-shadow: 0 2px 3px rgba(0,0,0,.3);
  }
  .title-top {
    position: absolute; left: 0; right: 0; top: 228px; text-align: center;
    font-weight: 900; font-size: 96px; letter-spacing: -0.01em;
    text-shadow: 0 5px 6px rgba(0,0,0,.35);
  }
  .title-band {
    position: absolute; left: 18px; right: 0; top: 348px; height: 134px;
    background: linear-gradient(180deg, var(--white), var(--band-light));
  }
  .title-key {
    position: absolute; left: 0; right: 0; top: 340px; text-align: center;
    font-weight: 900; font-size: 150px; color: var(--navy); letter-spacing: -0.01em;
    line-height: 1;
  }
  .title-end {
    position: absolute; left: 0; right: 0; top: 470px; text-align: center;
    font-weight: 900; font-size: 104px;
    text-shadow: 0 5px 6px rgba(0,0,0,.35);
  }
  .tagline, .subtitle {
    position: absolute; font-family: "Allura", cursive; color: var(--white);
    text-shadow: 0 2px 3px rgba(20,30,70,.45);
    white-space: nowrap;
  }
  .tagline {
    left: 230px; top: 610px; font-size: 72px;
    transform: rotate(10deg); transform-origin: left top;
  }
  .subtitle {
    left: 190px; top: 740px; font-size: 48px; line-height: 1.05;
    transform: rotate(12deg); transform-origin: left top;
  }
  .subtitle span { display: block; padding-left: 50px; }
  .endorsement {
    position: absolute; left: 0; right: 0; top: 985px; text-align: center;
  }
  .endorsement-quote { font-weight: 400; font-size: 30px; }
  .endorsement-name {
    font-weight: 800; font-size: 26px; letter-spacing: 0.06em; margin-top: 4px;
  }
</style>
</head>
<body>
  <main class="book-cover">
    <div class="cover-art" role="img" aria-label="Photograph: starry violet night sky over layers of misty blue mountains, with a figure leaping across the gap between two rocky cliffs"></div>

    <div class="author-band"></div>
    <p class="author-name">TESSA VARDEN</p>
    <p class="author-credit">Hollywood #1 Acting Coach</p>

    <h1>
      <span class="title-top">D*mn Those</span>
      <span class="title-band"></span>
      <span class="title-key">COZY</span>
      <span class="title-end">WALLS</span>
    </h1>

    <p class="tagline">Dare Boldly</p>
    <p class="subtitle">Claim Center Stage<span>Within Every Day</span></p>

    <blockquote class="endorsement">
      <p class="endorsement-quote">"I f*ucking love this book ...."</p>
      <p class="endorsement-name">JANELLE BROOKS</p>
    </blockquote>
  </main>
</body>
</html>
```